Young and modern Electrical company working in the commercial arena.

Wanting a business card design thats modern and will last. Maybe Minimalist? Happy to look at changing my logo

Target Market(s)

Builders, Project Managers

Industry/Entity Type

Electrical

Contact Information for Business Card

Name
Address
Phone number
Job title

Logo Text

our name or just the logo i'm open to ideas

Font styles to use
Sans Serif

Requirements
Nice to have
• would like to keep the purple in our current logo. it's kinda unique to our market
Should not have
• Don't want it to be to busy. simple is best i think

```html
<!DOCTYPE html>
<html lang="en">
<head>
<meta charset="utf-8">
<title>Halden Electrical – Business Card</title>
<link rel="stylesheet" href="https://fonts.googleapis.com/css2?family=Jost:wght@300;400;500;600&family=Open+Sans:wght@400;600&display=swap">
<style>
  :root {
    --purple: #512d82;
    --ink: #111111;
    --paper: #f2f2f2;
    --backdrop: #e6e4ea;
    --white: #ffffff;
  }
  * { margin: 0; padding: 0; box-sizing: border-box; }
  html, body {
    width: 1200px;
    height: 1200px;
    overflow: hidden;
    background: var(--backdrop);
  }
  .canvas {
    position: relative;
    width: 1200px;
    height: 1200px;
  }
  .card {
    position: absolute;
    left: 250px;
    width: 700px;
    height: 400px;
    background: var(--paper);
    overflow: hidden;
    box-shadow: 0 2px 8px rgba(0,0,0,0.12);
  }
  .card--front { top: 160px; }
  .card--back { top: 632px; }

  /* Front */
  .brand {
    position: absolute;
    left: 180px;
    top: 140px;
    display: flex;
    align-items: center;
    gap: 26px;
  }
  .brand__circle {
    width: 132px;
    height: 132px;
    border-radius: 50%;
    border: 6px solid var(--purple);
    flex: none;
  }
  .brand__name {
    font-family: "Jost", sans-serif;
    font-weight: 500;
    font-size: 44px;
    line-height: 1.0;
    color: var(--ink);
  }
  .brand__name span { display: block; }
  .front-band {
    position: absolute;
    left: 0;
    right: 0;
    bottom: 0;
    height: 14px;
    background: var(--purple);
    border-radius: 6px 6px 0 0;
  }

  /* Back */
  .name-panel {
    position: absolute;
    left: 0;
    top: 0;
    width: 100%;
    height: 296px;
    background: var(--purple);
    color: var(--white);
  }
  .person {
    position: absolute;
    left: 57px;
    top: 126px;
  }
  .person__name {
    font-family: "Jost", sans-serif;
    font-size: 50px;
    line-height: 1;
    font-weight: 300;
    letter-spacing: 0.5px;
  }
  .person__name strong { font-weight: 600; }
  .person__title {
    font-family: "Open Sans", sans-serif;
    font-size: 23px;
    font-weight: 400;
    margin-top: 2px;
    margin-left: 9px;
  }
  .contact {
    position: absolute;
    top: 328px;
    display: flex;
    gap: 8px;
    font-family: "Open Sans", sans-serif;
    font-weight: 600;
    font-size: 18px;
    line-height: 24px;
    color: var(--purple);
  }
  .contact--address { left: 116px; }
  .contact--phone { left: 384px; }
  .contact__icon { width: 20px; height: 22px; margin-top: 2px; flex: none; }
</style>
</head>
<body>
<main class="canvas">
  <section class="card card--front" aria-label="Card front">
    <div class="brand">
      <div class="brand__circle"></div>
      <p class="brand__name"><span>Halden</span><span>Electrical</span></p>
    </div>
    <div class="front-band"></div>
  </section>

  <section class="card card--back" aria-label="Card back">
    <div class="name-panel">
      <div class="person">
        <h1 class="person__name"><strong>YOUR</strong> NAME</h1>
        <p class="person__title">job title</p>
      </div>
    </div>

    <div class="contact contact--address">
      <svg class="contact__icon" viewBox="0 0 20 22" aria-hidden="true">
        <path d="M10 1.5a7 7 0 0 0-7 7c0 5 7 12 7 12s7-7 7-12a7 7 0 0 0-7-7z" fill="none" stroke="var(--purple)" stroke-width="2.4"/>
        <circle cx="10" cy="8.5" r="2.4" fill="var(--purple)"/>
      </svg>
      <p>123 loremipsum, lorem<br>loremipsum 78910</p>
    </div>

    <div class="contact contact--phone">
      <svg class="contact__icon" viewBox="0 0 20 22" aria-hidden="true">
        <path d="M4.5 2.5l3 .2 1.6 4.4-2 1.6c1 2.6 2.8 4.6 5.3 5.8l1.7-1.9 4.3 1.8v3.1c0 .8-.8 1.6-1.7 1.5C9 18.3 3 12 2.6 4.3c0-1 .8-1.8 1.9-1.8z" fill="var(--purple)"/>
      </svg>
      <p>+11 (0) 222 333 44 55</p>
    </div>
  </section>
</main>
</body>
</html>
```